Website for Pinegrove Tubing Tours

Require a website for a river float in the City of Edmonton. Located on North Saskatchewan River. Will need to be a coded website with incorporated booking system through Fare Harbor software.

Pages include
Home
Pricing
About
FAQ
Contact

Pinegrove Tubing Tours is an activity based business that will have customers floating down the North Saskatchewan river in Edmonton AB. The site will have all information needed and a full reservation system. The project was launched to provide people in the Edmonton area a favorite summer activity.

Here are similar websites to reference what our business will be doing and what we are looking for.

sunnybendpaddles.example
cedarcreekdrifts.example

Target Market(s)

Families, Groups, Individuals, Anyone who wants to explore the river

Industry/Entity Type

Activities based business/ Outdoor recreational/ River Float

Coding

Coded - Design and coding required

Number of Pages Required

5+ page

Colors
0054AA
0677BA
7BADD7
CADEEF
E8F1F8
F0912C
F2A743
F7CA91
FBE8D2
FDF5EE

```html
<!DOCTYPE html>
<html lang="en">
<head>
<meta charset="utf-8">
<title>Pinegrove Tubing Tours</title>
<link href="https://fonts.googleapis.com/css2?family=Exo+2:wght@700;800&family=Montserrat:wght@400;500;600;700&display=swap" rel="stylesheet">
<style>
:root{
  --navy:#0b2d5c;
  --blue-deep:#0054AA;
  --blue:#0677BA;
  --sky:#3fbde6;
  --blue-soft:#7BADD7;
  --blue-pale:#CADEEF;
  --blue-mist:#E8F1F8;
  --orange:#F0912C;
  --orange-soft:#F2A743;
  --cream:#FDF5EE;
  --ink:#1b2a3a;
  --muted:#5b6777;
  --white:#ffffff;
}
*{box-sizing:border-box;margin:0;padding:0}
html,body{width:1200px;height:4087px;overflow:hidden}
body{position:relative;background:var(--white);font-family:"Montserrat",sans-serif;color:var(--ink)}
.abs{position:absolute}
.heading{font-family:"Exo 2",sans-serif;font-weight:800;letter-spacing:1px}
.accent{color:var(--sky)}
.btn{position:absolute;display:flex;align-items:center;justify-content:center;font-weight:700;letter-spacing:1.5px;font-size:15px;color:var(--white);background:var(--orange);text-transform:uppercase}

/* header */
.hero{left:0;top:0;width:1200px;height:745px;background:linear-gradient(180deg,#e6ecf8 0%,#f3e4d6 28%,#d9c3a8 42%,#7a8b88 55%,#3c6a3a 68%,#2f5c46 82%,#5f8797 100%)}
.nav a{position:absolute;top:55px;font-size:13px;font-weight:700;letter-spacing:1px;color:var(--navy);text-decoration:none}
.nav a.current{color:var(--sky)}
.brand{left:470px;top:48px;width:260px;text-align:center;font-weight:700;font-size:19px;color:var(--navy);display:flex;align-items:center;justify-content:center;gap:8px}
.brand i{width:14px;height:14px;border-radius:50%;background:var(--sky);display:inline-block}
.nav-book{left:942px;top:58px;width:143px;height:34px;border-radius:17px;background:var(--sky);font-size:10px}
.hero-title{left:0;top:208px;width:1200px;text-align:center;font-size:54px;color:var(--navy)}
.hero-sub{left:0;top:310px;width:1200px;text-align:center;font-size:21px;color:var(--navy);font-weight:500}
.hero-book{left:508px;top:402px;width:178px;height:44px;border-radius:22px}

/* pricing */
.section-title{left:0;width:1200px;text-align:center;font-size:40px;color:var(--navy)}
.underline{height:4px;width:70px;background:var(--sky);border-radius:2px}
.photo-stack{position:absolute}
.photo-stack .back{position:absolute;inset:0;background:var(--white);box-shadow:0 6px 18px rgba(0,0,0,.2)}
.photo-stack .front{position:absolute;background:var(--white);box-shadow:0 6px 18px rgba(0,0,0,.25);padding:14px}
.photo-stack .fill{width:100%;height:100%}
.plan-name{left:643px;top:928px;font-size:27px;font-weight:700;letter-spacing:1px;color:var(--navy)}
.plan-price{left:643px;top:960px;font-size:28px;color:var(--orange);font-weight:700}
.plan-price span{font-weight:400}
.plan-intro{left:643px;top:1004px;width:480px;font-size:15px;line-height:24px;color:var(--navy)}
.ticks{list-style:none}
.ticks li{display:flex;align-items:center;gap:12px;height:38px;font-size:14.5px;color:var(--navy)}
.ticks svg{width:24px;height:24px;flex:none}
.price-book{left:554px;top:1289px;width:176px;height:45px}
.price-note{left:0;top:1350px;width:1268px;text-align:center;font-size:11.5px;color:var(--navy)}
.price-note u{text-decoration:underline}

/* about */
.about-band{left:0;top:1381px;width:1200px;height:746px}
.about-title{left:0;top:1530px;width:1200px;text-align:center;font-size:40px;color:var(--white)}
.about-sub{left:0;top:1610px;width:1200px;text-align:center;font-size:21px;line-height:26px;color:var(--white);font-weight:500}
.about-copy{left:160px;top:1676px;width:880px;text-align:center;font-size:15px;line-height:24px;color:var(--white)}
.about-copy p{margin-bottom:6px}
.about-book{left:528px;top:1928px;width:199px;height:51px;background:transparent;border:3px solid var(--white)}

/* faq */
.faq-title{left:135px;top:2232px;font-size:31px;color:var(--navy)}
.faq-list{left:135px;top:2300px;width:465px;list-style:none}
.faq-list li{height:50px;border-bottom:2px solid var(--blue-mist);display:flex;align-items:center;justify-content:space-between;font-size:14px;font-weight:700;color:var(--navy)}
.faq-list li.open{border-bottom:none}
.faq-answer{left:131px;top:2550px;width:400px;font-size:13px;line-height:21px;color:var(--ink)}
.faq-all{left:136px;top:2688px;width:183px;height:48px}
.cancel{left:136px;top:2766px;font-size:15px;color:var(--navy)}
.cancel u{text-decoration:underline}

/* contact */
.contact-band{left:0;top:2841px;width:1200px;height:730px}
.contact-title{left:0;top:2978px;width:1184px;text-align:center;font-size:36px;color:var(--white)}
.contact-greet{left:175px;top:3092px;font-size:19px;font-weight:700;color:var(--white)}
.contact-item{left:172px;display:flex;gap:18px;align-items:flex-start;color:var(--white)}
.contact-item .ico{width:48px;height:48px;border-radius:50%;background:var(--white);display:flex;align-items:center;justify-content:center;flex:none}
.contact-item .ico svg{width:26px;height:26px}
.contact-item small{display:block;font-size:15px;letter-spacing:1px;line-height:18px}
.contact-item strong{display:block;font-size:20px;letter-spacing:1px;margin-top:2px}
.contact-item strong.sm{font-size:14px}
.socials{left:182px;top:3400px;display:flex;gap:22px}
.socials span{width:30px;height:30px;background:var(--white)}
.socials span.round{border-radius:50%}
.map{left:579px;top:3079px;width:484px;height:349px;background:linear-gradient(135deg,#9cbcf0 0%,#c6e3cf 35%,#d8ecd9 70%,#f2f4f2 100%)}

/* footer */
.foot-head{top:3655px;font-size:15px;font-weight:700;color:var(--navy);font-family:"Exo 2",sans-serif;letter-spacing:.5px}
.foot-line{height:3px;width:40px;background:var(--sky)}
.foot-sub{left:162px;top:3702px;font-size:16px;font-weight:700;letter-spacing:1px;color:var(--navy)}
.foot-row{left:160px;display:flex;gap:10px;align-items:center;font-size:14px;color:var(--navy)}
.foot-row .dot{width:32px;height:32px;border-radius:50%;background:var(--blue-deep);display:flex;align-items:center;justify-content:center}
.foot-row .dot svg{width:17px;height:17px}
.foot-social{left:165px;top:3825px;display:flex;gap:22px}
.foot-social span{width:26px;height:26px;background:var(--blue)}
.foot-social span.round{border-radius:50%}
.foot-brand{left:490px;top:3745px;width:255px;text-align:center;font-size:22px;font-weight:700;color:var(--navy);display:flex;align-items:center;justify-content:center;gap:10px}
.foot-brand i{width:18px;height:18px;border-radius:50%;background:var(--sky)}
.foot-nav{left:936px;top:3700px;list-style:none}
.foot-nav li{font-size:16px;color:var(--navy);height:31px}
.rule{left:0;width:1200px;height:1px;background:var(--blue-pale)}
.mail-label{left:181px;top:3957px;font-size:16px;font-weight:700;letter-spacing:1px;color:var(--navy)}
.mail-input{left:511px;top:3947px;width:346px;height:40px;border-radius:20px;background:#e6e9ee;font-size:12px;color:var(--muted);padding:13px 24px}
.mail-btn{left:866px;top:3947px;width:159px;height:40px;border-radius:20px;font-size:13px;letter-spacing:1px;gap:6px}
.copyright{left:0;top:4029px;width:1200px;text-align:center;font-size:12px;color:var(--muted)}
</style>
</head>
<body>

<!-- Hero -->
<div class="abs hero" role="img" aria-label="Downtown Edmonton skyline above the river valley at sunset, with a bridge and green treed banks"></div>
<svg class="abs" style="left:0;top:610px" width="1200" height="140" viewBox="0 0 1200 140" aria-hidden="true">
  <path d="M0 60 L40 75 L70 62 L120 85 L170 70 L230 92 L290 78 L350 96 L420 84 L480 104 L540 92 L610 110 L670 96 L730 112 L790 98 L850 115 L910 100 L960 90 L1010 102 L1060 85 L1110 96 L1160 80 L1200 90 L1200 140 L0 140 Z" fill="#fff"/>
  <path d="M0 96 L60 104 L130 98 L200 110 L260 104 L330 118 L400 112 L470 124 L560 116 L640 128 L720 118 L800 126 L880 116 L960 124 L1040 110 L1120 118 L1200 104 L1200 140 L0 140 Z" fill="#fff"/>
</svg>

<nav class="nav">
  <a href="#" class="current" style="left:140px">HOME</a>
  <a href="#" style="left:238px">PRICING</a>
  <a href="#" style="left:354px">ABOUT</a>
  <a href="#" style="left:749px">FAQ</a>
  <a href="#" style="left:839px">CONTACT</a>
</nav>
<div class="abs brand"><i></i>Pinegrove Tubing Tours</div>
<div class="btn nav-book">Booking now</div>

<h1 class="abs heading hero-title">PINEGROVE <span class="accent">TUBING TOURS</span></h1>
<p class="abs hero-sub">Float the North Saskatchewan through downtown Edmonton</p>
<div class="btn hero-book">Book now ›</div>

<!-- Pricing -->
<h2 class="abs heading section-title" style="top:790px">OUR <span class="accent">PRICING</span></h2>
<div class="abs underline" style="left:565px;top:843px"></div>

<div class="photo-stack" style="left:108px;top:897px;width:495px;height:373px">
  <div class="back" style="left:0;top:0;width:480px;height:360px;transform:rotate(-3deg)"></div>
  <div class="front" style="left:18px;top:8px;width:470px;height:360px;transform:rotate(0deg)">
    <div class="fill" role="img" aria-label="Two smiling kids lying on colourful float tubes in the water" style="background:linear-gradient(135deg,#8fb7d3 0%,#e8c89a 40%,#d98a55 60%,#3e8fc7 100%)"></div>
  </div>
</div>

<h3 class="abs plan-name">TUBE AND SHUTTLE</h3>
<p class="abs plan-price">$30<span>/person</span></p>
<p class="abs plan-intro">We keep our pricing simple and include everything you need:<br>Premium comfort float tube with backrest and cup holder</p>
<ul class="abs ticks" style="left:645px;top:1064px">
  <li><svg viewBox="0 0 24 24"><circle cx="12" cy="12" r="12" fill="#3fbde6"/><path d="M7 12.5l3.2 3.2L17 9" stroke="#fff" stroke-width="2.4" fill="none" stroke-linecap="round" stroke-linejoin="round"/></svg>Lifejacket</li>
  <li><svg viewBox="0 0 24 24"><circle cx="12" cy="12" r="12" fill="#3fbde6"/><path d="M7 12.5l3.2 3.2L17 9" stroke="#fff" stroke-width="2.4" fill="none" stroke-linecap="round" stroke-linejoin="round"/></svg>Paddle</li>
  <li><svg viewBox="0 0 24 24"><circle cx="12" cy="12" r="12" fill="#3fbde6"/><path d="M7 12.5l3.2 3.2L17 9" stroke="#fff" stroke-width="2.4" fill="none" stroke-linecap="round" stroke-linejoin="round"/></svg>Round trip shuttle service</li>
  <li><svg viewBox="0 0 24 24"><circle cx="12" cy="12" r="12" fill="#3fbde6"/><path d="M7 12.5l3.2 3.2L17 9" stroke="#fff" stroke-width="2.4" fill="none" stroke-linecap="round" stroke-linejoin="round"/></svg>Safety training</li>
</ul>
<ul class="abs ticks" style="left:910px;top:1064px">
  <li><svg viewBox="0 0 24 24"><circle cx="12" cy="12" r="12" fill="#3fbde6"/><path d="M7 12.5l3.2 3.2L17 9" stroke="#fff" stroke-width="2.4" fill="none" stroke-linecap="round" stroke-linejoin="round"/></svg>Staff assistance</li>
  <li><svg viewBox="0 0 24 24"><circle cx="12" cy="12" r="12" fill="#3fbde6"/><path d="M7 12.5l3.2 3.2L17 9" stroke="#fff" stroke-width="2.4" fill="none" stroke-linecap="round" stroke-linejoin="round"/></svg>Parking</li>
  <li><svg viewBox="0 0 24 24"><circle cx="12" cy="12" r="12" fill="#3fbde6"/><path d="M7 12.5l3.2 3.2L17 9" stroke="#fff" stroke-width="2.4" fill="none" stroke-linecap="round" stroke-linejoin="round"/></svg>Unlimited Fun!</li>
</ul>
<div class="btn price-book">Book now</div>
<p class="abs price-note">Group of 10 or more? <u>Contact us</u> *does not include taxes or fees</p>

<!-- About -->
<svg class="abs about-band" viewBox="0 0 1200 746" preserveAspectRatio="none" role="img" aria-label="Blue brush band over a faded photo of people floating on tubes">
  <defs>
    <linearGradient id="aboutFill" x1="0" y1="0" x2="1" y2="1">
      <stop offset="0" stop-color="#3fc3ee"/><stop offset="0.55" stop-color="#1b8fd0"/><stop offset="1" stop-color="#0677BA"/>
    </linearGradient>
  </defs>
  <path d="M0 20 L60 12 L110 28 L170 6 L240 30 L300 14 L370 34 L430 18 L500 38 L570 24 L640 44 L700 30 L770 50 L840 38 L900 58 L960 46 L1030 70 L1090 60 L1150 82 L1200 74 L1200 690 L1150 700 L1080 680 L1010 712 L940 690 L870 724 L800 700 L730 736 L660 706 L590 726 L520 700 L450 716 L380 690 L310 704 L240 676 L170 690 L100 660 L40 672 L0 640 Z" fill="url(#aboutFill)"/>
</svg>
<h2 class="abs heading about-title">ABOUT PINEGROVE</h2>
<p class="abs about-sub">Float the North Saskatchewan through downtown Edmonton<br>Edmonton's Best Summer Activity</p>
<div class="abs about-copy">
  <p>We provide the lifejacket, paddle, river tube and shuttle service. You just have to show up. Pinegrove Tubing Tours was launched to provide people in the Edmonton area a favorite summer activity. Nothing is better on a hot summer day, than spending it on the river and seeing Edmonton from a new perspective.</p>
  <p>Our home base and meeting spot is at Willow Landing (Map Link), by the Glasshouse Conservatory. This is where you will check in, and board the shuttle. The shuttle will take all floaters up river to Aspen Park Boat Launch, where your tube will be waiting. Once on the river, you can sit back, relax, explore and enjoy the view. Once you complete the float, and arrive back at Willow Landing, staff will be available to assist in exiting the river where you will return your tube and gear. Safety is our top priority, but having fun is a close second.</p>
  <p>Don't miss out on Edmonton's best summer activity.</p>
</div>
<div class="btn about-book">Book now</div>

<!-- FAQ -->
<h2 class="abs heading faq-title">FREQUENTLY ASKED <span class="accent">QUESTIONS</span></h2>
<div class="abs underline" style="left:135px;top:2282px"></div>
<ul class="abs faq-list">
  <li>How do I reserve my float?<svg width="26" height="26" viewBox="0 0 26 26"><circle cx="13" cy="13" r="11.5" fill="none" stroke="#3fbde6" stroke-width="2"/><path d="M13 7v12M7 13h12" stroke="#3fbde6" stroke-width="2"/></svg></li>
  <li>What safety information should I know?<svg width="26" height="26" viewBox="0 0 26 26"><circle cx="13" cy="13" r="11.5" fill="none" stroke="#3fbde6" stroke-width="2"/><path d="M13 7v12M7 13h12" stroke="#3fbde6" stroke-width="2"/></svg></li>
  <li>What is included?<svg width="26" height="26" viewBox="0 0 26 26"><circle cx="13" cy="13" r="11.5" fill="none" stroke="#3fbde6" stroke-width="2"/><path d="M13 7v12M7 13h12" stroke="#3fbde6" stroke-width="2"/></svg></li>
  <li>What should I bring?<svg width="26" height="26" viewBox="0 0 26 26"><circle cx="13" cy="13" r="11.5" fill="none" stroke="#3fbde6" stroke-width="2"/><path d="M13 7v12M7 13h12" stroke="#3fbde6" stroke-width="2"/></svg></li>
  <li class="open">How long does the trip take?<svg width="26" height="26" viewBox="0 0 26 26"><circle cx="13" cy="13" r="11.5" fill="none" stroke="#0b2d5c" stroke-width="2"/><path d="M7 13h12" stroke="#0b2d5c" stroke-width="2"/></svg></li>
</ul>
<p class="abs faq-answer">Float times vary depending on a number of factors including river flow, and amount of paddling done during the float. The average float time is 3 hours, plus the 20-30min shuttle. Last floats of the day are limited to 3.5 hours, and encouraged to stay in the current.</p>
<div class="btn faq-all">View all</div>
<p class="abs cancel">To cancel, please email <u>info@pinegrovetubing.example</u> or call us.</p>

<div class="photo-stack" style="left:660px;top:2230px;width:455px;height:495px">
  <div class="back" style="left:40px;top:10px;width:400px;height:460px;transform:rotate(-2deg)"></div>
  <div class="front" style="left:10px;top:14px;width:435px;height:466px;transform:rotate(-4deg)">
    <div class="fill" role="img" aria-label="Woman relaxing on a yellow float tube on a green river below forested hills" style="background:linear-gradient(180deg,#4d7a3d 0%,#6a9a5a 30%,#4f8a86 55%,#c9b23a 78%,#e0c030 100%)"></div>
  </div>
</div>

<!-- Contact -->
<svg class="abs contact-band" viewBox="0 0 1200 730" preserveAspectRatio="none" role="img" aria-label="Deep blue brush band over a faded city skyline">
  <defs>
    <linearGradient id="contactFill" x1="0" y1="0" x2="0" y2="1">
      <stop offset="0" stop-color="#0a4f8f"/><stop offset="0.6" stop-color="#0b5aa5"/><stop offset="1" stop-color="#0a3f7a"/>
    </linearGradient>
  </defs>
  <path d="M0 30 L50 14 L110 34 L180 10 L240 36 L310 18 L380 40 L450 22 L520 46 L590 26 L660 48 L730 30 L800 52 L870 34 L940 56 L1010 38 L1080 60 L1140 44 L1200 62 L1200 690 L1140 672 L1070 700 L1000 682 L930 712 L860 690 L790 718 L720 694 L650 722 L580 698 L510 716 L440 692 L370 708 L300 682 L230 700 L160 676 L90 694 L30 668 L0 680 Z" fill="url(#contactFill)"/>
</svg>
<h2 class="abs heading contact-title">CONTACT PINEGROVE</h2>
<div class="abs underline" style="left:555px;top:3030px"></div>
<p class="abs contact-greet">We'd love to hear from you!</p>

<div class="abs contact-item" style="top:3140px">
  <span class="ico"><svg viewBox="0 0 24 24"><path d="M6.6 10.8a15.1 15.1 0 006.6 6.6l2.2-2.2c.3-.3.7-.4 1-.2 1.1.4 2.3.6 3.6.6.6 0 1 .4 1 1V20c0 .6-.4 1-1 1A17 17 0 013 4c0-.6.4-1 1-1h3.5c.6 0 1 .4 1 1 0 1.3.2 2.5.6 3.6.1.3 0 .7-.2 1z" fill="#0a4f8f"/></svg></span>
  <div><small>PHONE NUMBER</small><strong>(780) 555 0142</strong></div>
</div>
<div class="abs contact-item" style="top:3218px">
  <span class="ico"><svg viewBox="0 0 24 24"><rect x="3" y="5" width="18" height="14" rx="2" fill="#0a4f8f"/><path d="M4 7l8 6 8-6" stroke="#fff" stroke-width="1.6" fill="none"/></svg></span>
  <div><small>EMAIL ADDRESS</small><strong class="sm">info@pinegrovetubing.example</strong></div>
</div>
<div class="abs contact-item" style="top:3304px">
  <span class="ico"><svg viewBox="0 0 24 24"><path d="M12 2a7 7 0 00-7 7c0 5 7 13 7 13s7-8 7-13a7 7 0 00-7-7z" fill="#0a4f8f"/><circle cx="12" cy="9" r="2.6" fill="#fff"/></svg></span>
  <div><small>COME VISIT US ON FLOAT<br>DAYS AT WILLOW LANDING</small><strong class="sm" style="margin-top:6px">1200 Riverbend Rd NW, Edmonton, AB</strong></div>
</div>
<div class="abs socials"><span></span><span></span><span class="round"></span></div>
<div class="abs map" role="img" aria-label="Map showing the Willow Landing meeting spot beside the river"></div>

<!-- Footer -->
<h4 class="abs foot-head" style="left:157px">PINEGROVE TUBING TOURS</h4>
<div class="abs foot-line" style="left:157px;top:3680px"></div>
<p class="abs foot-sub">CONNECT</p>
<div class="abs foot-row" style="top:3730px"><span class="dot"><svg viewBox="0 0 24 24"><rect x="3" y="5" width="18" height="14" rx="2" fill="#fff"/><path d="M4 7l8 6 8-6" stroke="#0054AA" stroke-width="1.6" fill="none"/></svg></span>info@pinegrovetubing.example</div>
<div class="abs foot-row" style="top:3772px"><span class="dot"><svg viewBox="0 0 24 24"><path d="M12 2a7 7 0 00-7 7c0 5 7 13 7 13s7-8 7-13a7 7 0 00-7-7z" fill="#fff"/><circle cx="12" cy="9" r="2.6" fill="#0054AA"/></svg></span>Willow Landing</div>
<div class="abs foot-social"><span></span><span></span><span class="round"></span></div>

<h4 class="abs foot-head" style="left:502px">FLOATING 7 DAYS A WEEK</h4>
<div class="abs foot-line" style="left:502px;top:3680px"></div>
<div class="abs foot-brand"><i></i>Pinegrove Tubing Tours</div>

<h4 class="abs foot-head" style="left:928px">NAVIGATION</h4>
<div class="abs foot-line" style="left:928px;top:3680px"></div>
<ul class="abs foot-nav">
  <li>Home</li><li>Pricing</li><li>About Us</li><li>FAQ</li><li>Contact</li>
</ul>

<div class="abs rule" style="top:3920px"></div>
<p class="abs mail-label">SIGN UP FOR OUR MAILING LIST</p>
<div class="abs mail-input">Email address</div>
<div class="btn mail-btn">Subscribe<svg width="14" height="14" viewBox="0 0 24 24"><path d="M2 11l20-9-9 20-2-9z" fill="#fff"/></svg></div>
<div class="abs rule" style="top:4015px"></div>
<p class="abs copyright">© 2022 Pinegrove Tubing Tours &nbsp;All Rights Reserved</p>

</body>
</html>
```